Flat bootstrap design for existing site

I'm looking for a modern flat design based around an existing logo. This has to be a custom design (no external templates), and implemented into a bootstrap framework.

The logo is attached as 2 versions - choose whichever you want, that flows better with whatever design you choose.

Added screenshots of the existing site (currently using the default bootstrap layouts). Please make your designs around those pages in the screenshots (i.e. the homepage only has the postal code input and the header). The active page has 3 screenshots, because I wanted to illustrate the other states that would be visible (in the table rows).

This is a moving/junk removal website, just for some context.

Here's some example websites (flat designs) that I like, just to give you an idea of what I'm after.

https://www.plivoterra.com/
https://damsoqua.com/
https://trevalin.com/
https://morkadelphi.com/en/

Coding

Coded - Design and coding required

Number of Pages Required

5+ page

Colors

Designer to choose colors to be used in the design.

Requirements
Must have
• It must be a modern/simple flat design, that is built around the existing logo (attached).
• It has to be implemented using bootstrap.

```html
<!DOCTYPE html>
<html lang="en">
<head>
<meta charset="utf-8">
<title>HAULVEX – Invalid job code</title>
<link rel="stylesheet" href="https://fonts.googleapis.com/css2?family=Montserrat:wght@700;800&family=Rubik:wght@400&display=swap">
<style>
  :root {
    --sky: #3bbdf1;
    --sky-light: rgba(255, 255, 255, 0.28);
    --white: #ffffff;
    --ink: #2c2a3e;
    --driver-blue: #0f86cb;
    --signin-violet: #6a5ac8;
    --footer-ink: #3d3a6b;
    --social: #8f86b9;
  }
  * { margin: 0; padding: 0; box-sizing: border-box; }
  html, body {
    width: 1200px;
    height: 562px;
    overflow: hidden;
  }
  body {
    position: relative;
    background: var(--sky);
    font-family: "Rubik", Arial, sans-serif;
    color: var(--ink);
  }
  .site-header {
    position: absolute;
    left: 144px;
    right: 144px;
    top: 22px;
    height: 35px;
    display: flex;
    align-items: center;
    justify-content: space-between;
  }
  .brand {
    display: flex;
    align-items: center;
    gap: 8px;
    font-family: "Montserrat", Arial, sans-serif;
    font-weight: 800;
    font-size: 30px;
    color: var(--white);
    letter-spacing: 0.5px;
    text-decoration: none;
  }
  .brand-dot {
    width: 14px;
    height: 14px;
    border-radius: 50%;
    background: var(--white);
  }
  .main-nav {
    display: flex;
    align-items: center;
    font-family: "Montserrat", Arial, sans-serif;
    font-weight: 700;
    font-size: 11.5px;
    letter-spacing: 0.3px;
  }
  .nav-link {
    color: var(--white);
    text-decoration: none;
    margin-right: 26px;
  }
  .nav-button {
    display: flex;
    align-items: center;
    justify-content: center;
    height: 35px;
    color: var(--white);
    text-decoration: none;
    border-radius: 3px;
  }
  .nav-button.driver { width: 135px; background: var(--driver-blue); margin-left: 3px; }
  .nav-button.signin { width: 82px; background: var(--signin-violet); margin-left: 8px; }
  .notice-card {
    position: absolute;
    left: 144px;
    top: 102px;
    width: 912px;
    height: 56px;
    background: var(--white);
    border-radius: 4px;
    box-shadow: 0 6px 18px rgba(20, 90, 140, 0.22);
    padding: 0 22px;
    display: flex;
    align-items: center;
    font-size: 13px;
  }
  .hill {
    position: absolute;
    left: 1008px;
    top: 344px;
    width: 420px;
    height: 420px;
    border-radius: 50%;
    background: var(--sky-light);
  }
  .mover-scene {
    position: absolute;
    left: 1048px;
    top: 336px;
    width: 152px;
    height: 112px;
    border-radius: 6px;
    background: linear-gradient(160deg, #6fb3dc 0%, #4e9ed0 60%, #7cc08c 100%);
    opacity: 0.85;
  }
  .site-footer {
    position: absolute;
    left: 0;
    top: 497px;
    width: 1200px;
    height: 58px;
    background: var(--white);
    padding: 0 144px;
    display: flex;
    align-items: center;
    justify-content: space-between;
    font-size: 12px;
    color: var(--footer-ink);
  }
  .social-links { display: flex; gap: 6px; }
  .social-link {
    display: block;
    width: 19px;
    height: 19px;
    border-radius: 3px;
    background: var(--social);
  }
  .footer-band {
    position: absolute;
    left: 0;
    top: 555px;
    width: 1200px;
    height: 7px;
    background: var(--signin-violet);
  }
</style>
</head>
<body>
  <header class="site-header">
    <a class="brand" href="#"><span class="brand-dot"></span>HAULVEX</a>
    <nav class="main-nav">
      <a class="nav-link" href="#">BOOK</a>
      <a class="nav-link" href="#">HOW IT WORKS</a>
      <a class="nav-button driver" href="#">BECOME A DRIVER</a>
      <a class="nav-button signin" href="#">SIGNIN</a>
    </nav>
  </header>

  <main>
    <div class="notice-card">Invalid job code.</div>
  </main>

  <div class="hill"></div>
  <div class="mover-scene" role="img" aria-label="Illustration of a mover beside a bin, a house and a branded van"></div>

  <footer class="site-footer">
    <p class="copyright">© 2017 HAULVEX. All rights reserved.</p>
    <div class="social-links">
      <a class="social-link" href="#" aria-label="Social profile one"></a>
      <a class="social-link" href="#" aria-label="Social profile two"></a>
      <a class="social-link" href="#" aria-label="Social profile three"></a>
    </div>
  </footer>
  <div class="footer-band"></div>
</body>
</html>
```